Zielgruppe
für meinen ambulanten Pflegedienst hätte ich gerne Visitenkarten. #
Für zwei Personen mir jeweils gleicher Geschäftsadresse.
KaLuVo Die flinke Pflegehilfe GmbH
www.Kaluvo.de
Das Logo bitte der Homepage entnehmen.
Entwurf bitte für eine Visitenkarte und Briefpapier
Des weiteren wird ein Design für einen runden Leuchtkasten Durchmesser 90 cm benötigt.
Auf dem Briefpapier ist dass noch Kontonummer und Steuernummer zu ergänzen
Aufgabenstellung
Die Visitenkarte sollte elegant und luxuriös sein.

```html
<!DOCTYPE html>
<html lang="de">
<head>
<meta charset="utf-8">
<title>KaLuVo – Visitenkarte</title>
<link rel="stylesheet" href="https://fonts.googleapis.com/css2?family=Figtree:wght@300;400;500&display=swap">
<style>
  :root {
    --page: #ffffff;
    --card: #ffffff;
    --green: #4f8a35;
    --red: #a8232b;
    --text: #4a4a4a;
    --rule: #3a3a3a;
  }
  * { margin: 0; padding: 0; box-sizing: border-box; }
  html, body { width: 1200px; height: 2298px; overflow: hidden; background: var(--page); }
  body { position: relative; font-family: "Figtree", Arial, sans-serif; color: var(--text); }

  .card {
    position: absolute;
    left: 285px;
    width: 630px;
    height: 418px;
    background: var(--card);
    box-shadow: 6px 10px 14px rgba(0,0,0,0.22);
  }
  .card--front { top: 648px; }
  .card--back { top: 1233px; }

  /* front */
  .brand {
    position: absolute;
    display: flex;
    align-items: center;
    gap: 12px;
  }
  .brand__square { background: var(--red); }
  .brand__name { color: var(--green); font-weight: 400; letter-spacing: 0.5px; }

  .card--front .brand { left: 60px; top: 172px; }
  .card--front .brand__square { width: 26px; height: 26px; }
  .card--front .brand__name { font-size: 40px; }

  .divider { position: absolute; left: 315px; width: 1.5px; background: var(--rule); }
  .divider--name { top: 56px; height: 73px; }
  .divider--contact { top: 192px; height: 163px; }

  .person { position: absolute; left: 332px; top: 56px; }
  .person__name { color: var(--green); font-size: 20px; font-weight: 400; line-height: 24px; }
  .person__title { font-size: 16px; font-weight: 300; line-height: 22px; }

  .contact { position: absolute; left: 339px; font-size: 15.5px; font-weight: 300; line-height: 22.5px; display: flex; gap: 7px; }
  .contact svg { width: 13px; height: 13px; margin-top: 5px; flex: none; fill: var(--green); }
  .contact--phone { top: 188px; }
  .contact--mail { top: 256px; }
  .contact--address { top: 300px; }

  /* back */
  .card--back .brand { left: 0; right: 0; top: 150px; justify-content: center; gap: 18px; }
  .card--back .brand__square { width: 44px; height: 44px; }
  .card--back .brand__name { font-size: 64px; }

  .website { position: absolute; left: 0; right: 0; top: 338px; display: flex; align-items: center; justify-content: center; gap: 26px; }
  .website__rule { width: 166px; height: 1.5px; background: var(--rule); }
  .website__url { font-size: 18px; font-weight: 400; }
</style>
</head>
<body>
  <section class="card card--front">
    <div class="brand">
      <span class="brand__square"></span>
      <span class="brand__name">KaLuVo</span>
    </div>

    <span class="divider divider--name"></span>
    <div class="person">
      <p class="person__name">NAME SURNAME</p>
      <p class="person__title">Job title</p>
    </div>

    <span class="divider divider--contact"></span>
    <div class="contact contact--phone">
      <svg viewBox="0 0 24 24" aria-hidden="true"><path d="M6.6 10.8a15.2 15.2 0 0 0 6.6 6.6l2.2-2.2c.3-.3.7-.4 1-.2 1.1.4 2.3.6 3.6.6.6 0 1 .4 1 1V20c0 .6-.4 1-1 1A17 17 0 0 1 3 4c0-.6.4-1 1-1h3.5c.6 0 1 .4 1 1 0 1.3.2 2.5.6 3.6.1.3 0 .7-.2 1z"/></svg>
      <p>030555-214087<br>01725550193</p>
    </div>
    <div class="contact contact--mail">
      <svg viewBox="0 0 24 24" aria-hidden="true"><path d="M2 5h20v14H2z M3.5 6.5 12 13l8.5-6.5" stroke="#fff" stroke-width="1.6"/></svg>
      <p>Lindner@Kaluvo.de</p>
    </div>
    <div class="contact contact--address">
      <svg viewBox="0 0 24 24" aria-hidden="true"><path d="M12 2a7 7 0 0 0-7 7c0 5.2 7 13 7 13s7-7.8 7-13a7 7 0 0 0-7-7zm0 9.5a2.5 2.5 0 1 1 0-5 2.5 2.5 0 0 1 0 5z"/></svg>
      <p>KaLuVo<br>Die flinke Pflegehilfe GmbH<br>Lindenweg 12<br>12345 Musterstadt</p>
    </div>
  </section>

  <section class="card card--back">
    <div class="brand">
      <span class="brand__square"></span>
      <span class="brand__name">KaLuVo</span>
    </div>
    <div class="website">
      <span class="website__rule"></span>
      <span class="website__url">www.kaluvo.de</span>
      <span class="website__rule"></span>
    </div>
  </section>
</body>
</html>
```